Business card design and logo for plumbing bussiness

We are wanting a logo for a plumbing business is Queensland Australia. KRV Plumbing and Drainage will be doing works on domestic and commercial sites.
Plumbing, drainage and gas works. We are wanting something that will stand out and be noticed. Colours could be black blue and white but open for suggestions.

Target Market(s)

Builders and home renovators

Industry/Entity Type

Plumbing

Contact Information for Business Card

Miles Dorgan - Director
0417 582 913
miles@krvplumbing.example.com.au
QBCC: 847 2106
ABN: 52 319 407 281

Font styles to use
Sans Serif

Colors
000000

Requirements
Must have
• Clear defined branding

```html
<!DOCTYPE html>
<html lang="en">
<head>
<meta charset="utf-8">
<title>KRV Plumbing and Drainage – Business Card</title>
<link href="https://fonts.googleapis.com/css2?family=Lato:wght@300;400;700&display=swap" rel="stylesheet">
<style>
  :root {
    --backdrop: #dcdcdc;
    --card: #f7f7f7;
    --ink: #1a1a1a;
    --accent: #0a9fdc;
    --rule: #333333;
  }
  * { margin: 0; padding: 0; box-sizing: border-box; }
  html, body {
    width: 1200px; height: 899px; overflow: hidden;
    background: var(--backdrop);
    font-family: "Lato", Arial, sans-serif;
    color: var(--ink);
  }
  .card {
    position: absolute;
    left: 300px;
    width: 600px; height: 366px;
    background: var(--card);
    box-shadow: 0 2px 8px rgba(0,0,0,0.12);
    overflow: hidden;
  }
  .card--front { top: 48px; }
  .card--back  { top: 480px; }

  .band {
    position: absolute;
    height: 34px;
    background: var(--accent);
  }
  .card--front .band--left  { left: 0; width: 215px; top: 135px; }
  .card--front .band--right { left: 405px; right: 0; top: 195px; }

  .brand {
    position: absolute;
    font-weight: 700;
    color: var(--ink);
    white-space: nowrap;
  }
  .card--front .brand {
    left: 232px; top: 148px;
    font-size: 20px; line-height: 26px;
  }

  .card--back .band--top  { left: 320px; right: 0; top: 72px; height: 28px; }
  .card--back .band--logo { left: 0; width: 120px; top: 118px; height: 28px; }
  .card--back .brand { left: 132px; top: 112px; font-size: 18px; line-height: 24px; }

  .person {
    position: absolute;
    right: 40px; top: 22px;
    text-align: right;
  }
  .person__name { font-weight: 700; font-size: 20px; letter-spacing: 0.4px; text-transform: uppercase; }
  .person__role { font-weight: 300; font-size: 15px; margin-top: -2px; }

  .contacts {
    position: absolute;
    left: 60px; top: 176px;
    width: 270px;
    list-style: none;
    font-size: 14px; line-height: 17px;
  }
  .contacts__item {
    border-top: 1px solid var(--rule);
    padding: 8px 0 10px;
  }
  .contacts__icon { display: block; width: 18px; height: 16px; margin-bottom: 3px; }
</style>
</head>
<body>

<section class="card card--front" aria-label="Card front">
  <div class="band band--left"></div>
  <div class="band band--right"></div>
  <div class="brand">KRV Plumbing<br>and Drainage</div>
</section>

<section class="card card--back" aria-label="Card back">
  <div class="person">
    <div class="person__name">Miles Dorgan</div>
    <div class="person__role">Director</div>
  </div>
  <div class="band band--top"></div>
  <div class="band band--logo"></div>
  <div class="brand">KRV Plumbing<br>and Drainage</div>

  <ul class="contacts">
    <li class="contacts__item">
      <svg class="contacts__icon" viewBox="0 0 18 16" aria-hidden="true">
        <circle cx="5" cy="2.5" r="2" fill="var(--accent)"/>
        <path d="M3 6h4v8h2v2H1v-2h2V8H1V6z" fill="var(--accent)"/>
      </svg>
      QBCC: 847 2106<br>ABN: 52 319 407 281
    </li>
    <li class="contacts__item">
      <svg class="contacts__icon" viewBox="0 0 18 16" aria-hidden="true">
        <rect x="1" y="3" width="16" height="11" fill="var(--accent)"/>
        <path d="M1 3l8 6 8-6" fill="none" stroke="#ffffff" stroke-width="1.4"/>
      </svg>
      miles@krvplumbing.example.com.au
    </li>
    <li class="contacts__item">
      <svg class="contacts__icon" viewBox="0 0 18 16" aria-hidden="true">
        <circle cx="8" cy="8" r="7" fill="none" stroke="var(--accent)" stroke-width="1.5"/>
        <path d="M5.5 4.5l1.5-.5 1 2-1 1c.5 1.2 1.3 2 2.5 2.5l1-1 2 1-.5 1.5c-3 .3-6.8-3.5-6.5-6.5z" fill="var(--accent)"/>
      </svg>
      0417 582 913
    </li>
  </ul>
</section>

</body>
</html>
```